Business Card Design

Lintel Comms is a public relations consultancy service for the self build, home refurbishment and home improvement market.
It represents everything about 'home' so envisage logo featuring maybe roof pitch over the 'A' of Lintel. Colour/font undecided.

Industry/Entity Type

Home Improvement

Contact Information for Business Card

Fenella Coxworth
fenella@lintelcomms.co.uk
Telephone Direct: 0788 142 6597

```html
<!DOCTYPE html>
<html lang="en">
<head>
<meta charset="utf-8">
<title>Lintel Comms – Business Card</title>
<link rel="stylesheet" href="https://fonts.googleapis.com/css2?family=Cardo:ital,wght@0,400;0,700;1,400&display=swap">
<style>
  :root {
    --backdrop: #e8e4df;
    --wood-light: #d27a2c;
    --wood-mid: #b45a1c;
    --wood-dark: #7e3410;
    --band: #ffffff;
    --brand-brown: #9a4a16;
    --ink-light: #ffffff;
  }
  * { box-sizing: border-box; margin: 0; padding: 0; }
  html, body {
    width: 1200px; height: 720px; overflow: hidden;
    background: var(--backdrop);
  }
  .canvas {
    position: relative; width: 1200px; height: 720px;
  }
  .card {
    position: absolute; left: 100px; top: 74px;
    width: 1000px; height: 572px;
    overflow: hidden;
    font-family: "Cardo", Georgia, serif;
    color: var(--ink-light);
    box-shadow: 0 10px 30px rgba(0,0,0,0.25);
  }
  .card__wood {
    position: absolute; inset: 0;
    background:
      radial-gradient(ellipse 45% 40% at 52% 48%, rgba(255,220,160,0.35), rgba(255,220,160,0) 70%),
      linear-gradient(90deg, var(--wood-dark) 0%, var(--wood-mid) 22%, var(--wood-light) 50%, var(--wood-mid) 78%, var(--wood-dark) 100%);
  }
  .brand-band {
    position: absolute; left: 0; right: 0; top: 150px; height: 84px;
    background: var(--band);
    display: flex; align-items: center; justify-content: space-between;
    padding: 0 40px 0 34px;
  }
  .brand-band__name {
    font-size: 44px; font-weight: 400; letter-spacing: 1px;
    color: var(--brand-brown); line-height: 1;
    white-space: nowrap;
  }
  .brand-band__mark {
    flex: none;
    width: 52px; height: 52px; border-radius: 50%;
    background: var(--brand-brown);
  }
  .person {
    position: absolute; top: 282px; right: 540px;
    text-align: right; white-space: nowrap;
  }
  .person__name { font-size: 38px; font-weight: 700; letter-spacing: 0.5px; line-height: 1.1; }
  .person__note { font-size: 26px; font-style: italic; margin-top: 6px; }
  .divider {
    position: absolute; left: 496px; top: 262px;
    width: 4px; height: 128px; background: var(--ink-light);
  }
  .contact {
    position: absolute; left: 532px; top: 272px;
    font-size: 27px; line-height: 1.6; white-space: nowrap;
    display: grid; grid-template-columns: auto auto; column-gap: 16px;
  }
  .contact__label { font-weight: 700; }
</style>
</head>
<body>
  <div class="canvas">
    <article class="card">
      <div class="card__wood" role="img" aria-label="Warm orange-brown wood grain texture background"></div>

      <div class="brand-band">
        <h1 class="brand-band__name">Lintel Comms Home Improvement</h1>
        <span class="brand-band__mark" aria-hidden="true"></span>
      </div>

      <div class="person">
        <p class="person__name">Fenella Coxworth</p>
        <p class="person__note">Fully Insured</p>
      </div>

      <div class="divider" aria-hidden="true"></div>

      <dl class="contact">
        <dt class="contact__label">Phone:</dt>
        <dd class="contact__value">0788 142 6597</dd>
        <dt class="contact__label">Email:</dt>
        <dd class="contact__value">fenella@lintelcomms.co.uk</dd>
      </dl>
    </article>
  </div>
</body>
</html>
```